Dog Daycare Facility needs a New Doggo welcome packet!

We are Bright Meadow Pet Play Lodge, a dog daycare, training, boarding and grooming facility in Iowa. We have recently grown our outdoor yards and are seeing a lot of new dogs, and want to create a professional, clean folder for new dogs that go through our evaluation process. We need multiple pages, highlighting different facets of our business. We have our brand that we use through our facility (our logo, the color lime green, and the outline of the state of Iowa to a lesser degree) and would like them to be included somehow. We will use either stock photos of dogs outside or any design/art drawings to keep the packet cohesive.

The first page is a full 8 ½ x 11 sheet that will slide into each dog’s folder as the front insert. We would like this to be bright, fun and inviting without being too busy. We would like basic information on the front page: Our business (Bright Meadow), address (4815 W. Orchard Rd., Cedar Falls, IA 50613), phone number (319-555-0182), and a cute spot for the dog’s name to be written down. Think name tag or collar or dog tag. We have a fairly strong printer so colors and vivid photos shouldn’t be a problem. We want to remain professional while still looking fun!

We want to have a few handouts about the services we offer. These can be either organized on 8 ½ x 11 sheets, or if it looks clean have smaller 5x7 individual sheets with the information on them. Here’s what we want on each of the four sheets:

#1: Dog Daycare

We offer daycare Monday through Saturday, where dogs are put in groups based on their size, temperament, breed, play styles and energy levels. We have seven outdoor play yards and two indoor yards for inclement weather. All of our dogs stay in yards, learning socialization skills and playing with other pups, through the morning until about 11am. At that point our dogs go up for naptime, to give them a breather, give lunches for dogs whose owners want them fed, and a quiet moment to relax. Our dogs do a lot of running and jumping, so they really need a moment to give their legs a break. Once it’s 1, they go back out for the afternoon to socialize, play games and explore our yards again. Our hours are 6am-7pm Monday through Friday, 9am-5:30pm on Saturday. We are interested in having this as a handout, and having our hours listed on a magnet, so a small image that we can print on magnets would be awesome.

#2: Boarding

Every dog that stays with us for boarding automatically gets put in our Daycare, so they spend much less time in kennels than other facilities. The benefit of our boarding is each dog gets their own space to rest and relax. Our suites are spacious and come furnished with a Pellovi bed, blankets, and windows so the room doesn’t feel too small. Our presidential suites even come with TVs, to stretch out and watch animal documentaries. For our more frugal pups, we offer small and large Economy boarding, sized right for your dog to move around freely while staying safe and warm in their kennels. We encourage bringing a blanket from home and toys they love, so their room feels like theirs. We always provide extra blankets and bowls for food and water, keeping our pups as comfy as possible! Pricing is available on our website (pawsplayhousehub.example) for examples.

#3: Training

A growing part of our business, we have three staff dedicated to training dogs every day. Our Board and Train program is an intensive 28-day regiment of structured training sessions throughout the day, with group training and group play in our yards with other training dogs. Our Daycare and Train program follows the same regiment of one-on-one training, group trains and play in our yards, but you take your pup home after the day! Enroll your dog and work through our Bachelors, Masters, and Doctorate in dog behaviors, with flexible programs to best fit your life! We have a lot of information on our website about both the Daycare and Train and Board and Train programs, so if it’s cohesive and clean we can do a full page, but it should be easy to follow – our clients tend to get the full explanation when they inquire about training.

#4: Grooming

Getting your dog groomed makes them look and smell amazing. It can also help with their overall health and happiness! Bright Meadow has a great team that can provide your dog with a bath, nail trim, brush outs and more. If your dog is using one of our many services, we highly recommend a Go-Home Bath prior to departure. We have many outdoor play areas and it’s very common for pets to get a little dirty when out playing with their friends. Request a reservation today to get your pup looking and feeling their best!

Spa Day

Let us clean up muddy paws with this inclusive service of a brush out, nail trim, ear cleaning, and deep cleansing bath – topped off with dog-safe cologne!

Trim Groom

All of the comforts of a spa day, with an added feathering cut! This is done specifically for dogs with furnishings (think the back legs of Golden Retrievers and Brittany’s).

Haircut

If your pet has longer fur and fluff, choose the Haircut to receive a brush out, nail trim, ear cleaning, and a refreshing bath with comfortable drying. Afterwards, your dog’s fur is cut to the desired length, including close trimming for sanitation and foot pads in addition to their full body cut. If you want anything specifically shorter/left long, just request it from our groomer!

Again, there is a ton of information on our website (www.pawsplayhousehub.example/dog-grooming/) , and this one should have prices, brief explanation of the services we provide, and help the owner know what they can get from our services based on the size and breed of their pup. The Grooming page should be an 8 ½ x 11 for sure, as customers have a lot of questions initially about our services.

Please feel free to ask any questions about our project and if you have any ideas you wanted to bounce before creating let us know! We're excited to see what you come up with!

Font styles to use
Serif

Colors
acd036
ffffff

Requirements
Nice to have
• We're aiming for cute while being professional. We want some original art if it matches our brand and our logo style.

```html
<!DOCTYPE html>
<html lang="en">
<head>
<meta charset="utf-8">
<title>Dog Daycare Handout</title>
<link rel="stylesheet" href="https://fonts.googleapis.com/css2?family=Patrick+Hand&family=Oswald:wght@500&family=Poppins:wght@400&display=swap">
<style>
  :root {
    --lime: #acd036;
    --lime-soft: #c4df6e;
    --paw-tint: #f4f8ec;
    --white: #ffffff;
    --backdrop: #f1f2ef;
    --ink: #4a4a4a;
    --wood-light: #e2b77a;
    --wood-dark: #c98f4c;
    --wood-ink: #5a3718;
    --card-shadow: rgba(0, 0, 0, 0.14);
  }
  * { margin: 0; padding: 0; box-sizing: border-box; }
  html, body {
    width: 797px; height: 1200px; overflow: hidden;
    background: var(--backdrop);
  }
  .sheet {
    position: absolute; left: 0; top: 84px;
    width: 797px; height: 1031px;
    background: var(--white);
    box-shadow: 0 2px 8px rgba(0, 0, 0, 0.08);
    overflow: hidden;
  }
  .paw-pattern {
    position: absolute; inset: 0;
    background:
      linear-gradient(90deg, var(--paw-tint) 0%, var(--white) 22%, var(--white) 78%, var(--paw-tint) 100%);
  }
  .title-tag {
    position: absolute; left: 166px; top: 45px;
    width: 466px; height: 169px;
    border-radius: 60px;
    background: linear-gradient(180deg, var(--lime-soft), var(--lime) 60%);
  }
  .title {
    position: absolute; left: 166px; top: 108px; width: 466px;
    text-align: center;
    font-family: "Patrick Hand", cursive;
    font-size: 46px; letter-spacing: 1px; font-weight: 400;
    color: var(--white);
    line-height: 56px;
  }
  .info-card {
    position: absolute; left: 97px; top: 261px;
    width: 600px; height: 717px;
    background: var(--white);
    border-radius: 58px;
    box-shadow: 0 6px 10px var(--card-shadow), 0 0 3px rgba(0,0,0,0.06);
  }
  .hours-plank {
    position: absolute; left: 198px; top: 242px;
    width: 402px; height: 96px;
    transform: rotate(-3deg);
    border-radius: 3px;
    background: linear-gradient(180deg, var(--wood-light), var(--wood-dark) 55%, var(--wood-light));
    box-shadow: 0 3px 5px rgba(0,0,0,0.2);
    display: flex; flex-direction: column; justify-content: center; align-items: center;
  }
  .hours-plank p {
    font-family: "Oswald", sans-serif; font-weight: 500;
    font-size: 22px; line-height: 30px;
    color: var(--wood-ink);
    text-transform: uppercase;
  }
  .intro {
    position: absolute; left: 143px; top: 378px; width: 512px;
    font-family: "Poppins", sans-serif; font-size: 13.4px; line-height: 24px;
    letter-spacing: -0.1px;
    color: var(--ink);
  }
  .schedule-row { position: absolute; left: 146px; width: 490px; }
  .schedule-time {
    position: absolute; left: 0; top: 0;
    display: flex; align-items: flex-start;
    font-family: "Oswald", sans-serif; font-size: 14px; line-height: 16px;
    color: var(--ink); text-transform: uppercase; letter-spacing: -0.2px;
  }
  .schedule-time svg { width: 24px; height: 24px; margin-right: -4px; margin-top: -6px; }
  .schedule-text {
    position: absolute; left: 207px; top: -6px; width: 277px;
    font-family: "Poppins", sans-serif; font-size: 13.4px; line-height: 24px;
    color: var(--ink); text-align: justify;
  }
</style>
</head>
<body>
  <main class="sheet">
    <div class="paw-pattern" role="img" aria-label="Faint pale green paw-print pattern across the page"></div>

    <div class="title-tag" role="img" aria-label="Lime green bone-shaped name tag illustration"></div>
    <h1 class="title">DOG DAYCARE</h1>

    <section class="info-card" aria-label="Daycare details"></section>

    <div class="hours-plank" role="img" aria-label="Wooden sign showing opening hours">
      <p>6am-7pm Monday- Friday</p>
      <p>9am-5:30pm on Saturday</p>
    </div>

    <p class="intro">We offer daycare Monday through Saturday, where dogs are put in groups based on their size, temperament, breed, play styles and energy levels.&nbsp; We have seven outdoor play yards and two indoor yards for inclement weather.</p>

    <div class="schedule-row" style="top:546px">
      <div class="schedule-time">
        <svg viewBox="0 0 24 24" aria-hidden="true"><g fill="var(--lime)"><ellipse cx="12" cy="16" rx="5" ry="4.5"/><circle cx="5" cy="10" r="2.3"/><circle cx="9" cy="6" r="2.3"/><circle cx="15" cy="6" r="2.3"/><circle cx="19" cy="10" r="2.3"/></g></svg>
        <span>Morning until 11 am</span>
      </div>
      <p class="schedule-text">All of our dogs stay in yards, learning socialization skills and playing with other pups</p>
    </div>

    <div class="schedule-row" style="top:648px">
      <div class="schedule-time">
        <svg viewBox="0 0 24 24" aria-hidden="true"><g fill="var(--lime)"><ellipse cx="12" cy="16" rx="5" ry="4.5"/><circle cx="5" cy="10" r="2.3"/><circle cx="9" cy="6" r="2.3"/><circle cx="15" cy="6" r="2.3"/><circle cx="19" cy="10" r="2.3"/></g></svg>
        <span>11 am</span>
      </div>
      <p class="schedule-text">At that point our dogs go up for naptime, to give them a breather, give lunches for dogs whose owners want them fed, and a quiet moment to relax. Our dogs do a lot of running and jumping, so they really need a moment to give their legs a break.</p>
    </div>

    <div class="schedule-row" style="top:848px">
      <div class="schedule-time">
        <svg viewBox="0 0 24 24" aria-hidden="true"><g fill="var(--lime)"><ellipse cx="12" cy="16" rx="5" ry="4.5"/><circle cx="5" cy="10" r="2.3"/><circle cx="9" cy="6" r="2.3"/><circle cx="15" cy="6" r="2.3"/><circle cx="19" cy="10" r="2.3"/></g></svg>
        <span>1 pm</span>
      </div>
      <p class="schedule-text">They go back out for the afternoon to socialize, play games and explore our yards again.</p>
    </div>
  </main>
</body>
</html>
```